Escrow Accounting firm needs a website design for a startup that services clients nationally.

I offer escrow accounting services for title companies and real estate attorneys. I've enclosed a logo, color palette and flyers with content that can be used for the site.

I'm looking for a similar design concept as the website below from my former employer. Please don't copy because of copyright infringement. Including for design ideas only.
www.harborlinefiduciary.com

Below is a brief write-up...
For professionals in the title insurance industry, finding a trustworthy and budget-friendly solution for escrow accounting can be daunting. When choosing the right accounting partner, title companies and law firms need a group they can rely on, and that's where we come in.

```html
<!DOCTYPE html>
<html lang="en">
<head>
<meta charset="utf-8">
<title>Meridian Escrow Partners</title>
<link rel="stylesheet" href="https://fonts.googleapis.com/css2?family=Montserrat:wght@400;500;600;700;800&display=swap">
<style>
:root{
  --clay:#b9725d;
  --clay-soft:#e7c6bb;
  --clay-line:#d9a898;
  --navy:#343c4b;
  --ink:#3d4350;
  --text:#555b66;
  --mist:#eeeeef;
  --white:#ffffff;
}
*{box-sizing:border-box;margin:0;padding:0}
html,body{width:1200px;height:4391px;overflow:hidden}
body{font-family:'Montserrat',sans-serif;color:var(--text);background:var(--white)}
.page{position:relative;width:1200px;height:4391px;overflow:hidden;background:var(--white)}
.abs{position:absolute}
svg.abs{display:block}

/* header */
.site-header{position:absolute;left:0;top:0;width:1200px;height:80px;background:var(--white);z-index:5}
.brand{position:absolute;left:89px;top:12px;display:flex;align-items:center;gap:12px;color:var(--clay)}
.brand-square{width:34px;height:34px;background:var(--clay);transform:rotate(45deg);margin:0 6px}
.brand-name{font-weight:600;font-size:27px;line-height:27px;letter-spacing:.5px}
.brand-name small{display:block;font-size:15.5px;line-height:17px;letter-spacing:1.4px}
.main-nav a{position:absolute;top:32px;font-size:13px;font-weight:500;color:var(--ink);text-decoration:none;letter-spacing:.2px}
.main-nav a.active{color:var(--clay);font-weight:700}
.header-phone{position:absolute;left:926px;top:18px;display:flex;align-items:center;gap:14px;font-weight:700;font-size:20px;color:var(--ink)}
.phone-mark{width:30px;height:30px;background:var(--clay);transform:rotate(45deg);border-radius:6px;display:flex;align-items:center;justify-content:center}
.phone-mark svg{transform:rotate(-45deg)}

/* hero */
.hero-title{position:absolute;left:87px;top:190px;font-size:73px;line-height:69px;color:var(--navy);font-weight:400;letter-spacing:1px}
.hero-title b{display:block;color:var(--clay);font-weight:800}
.hero-sub{position:absolute;left:89px;top:414px;font-size:11px;font-weight:600;color:var(--ink)}
.btn{position:absolute;display:flex;align-items:center;justify-content:center;font-size:12.5px;font-weight:700;color:var(--white);text-decoration:none;letter-spacing:.3px;border-radius:4px 20px 4px 20px}
.btn-clay{background:var(--clay)}
.btn-navy{background:var(--navy)}
.slider-dots{position:absolute;left:567px;top:701px;display:flex;gap:14px}
.slider-dots i{width:12px;height:12px;border-radius:50%;background:#fff;box-shadow:0 0 2px rgba(0,0,0,.3)}

/* what we do */
.section-heading{font-size:40px;font-weight:800;color:var(--navy);letter-spacing:.5px;line-height:1.05}
.section-heading em{font-style:normal;color:var(--clay)}
.about-copy{position:absolute;left:692px;top:900px;width:410px}
.about-copy p{font-size:13.5px;line-height:19.6px;margin-top:12px}
.about-copy .lead{font-size:12.5px;font-weight:700;color:var(--ink);line-height:19px;margin-top:20px}

/* services */
.service-bar{position:absolute;left:179px;width:600px;height:72px;background:var(--clay);clip-path:polygon(18px 0,100% 0,100% 100%,18px 100%,0 50%);display:flex;align-items:center;padding-left:108px;color:var(--white);font-weight:700;font-size:15.5px;letter-spacing:.2px}
.service-bar svg{position:absolute;left:58px;top:18px}
.services-card{position:absolute;left:654px;top:1332px;width:370px;height:370px;text-align:center}
.services-card .section-heading{font-size:40px;line-height:41px}
.services-card p{font-size:14px;line-height:19.5px;margin:14px auto 0;width:240px;color:var(--ink)}

/* team */
.team-heading{position:absolute;left:89px;top:1935px;font-size:40px;line-height:44px;font-weight:800;color:var(--navy)}
.team-heading em{font-style:normal;color:var(--clay)}
.team-sub{position:absolute;left:89px;top:2083px;font-size:22px;font-weight:500;color:var(--navy)}

/* features */
.feature-text{position:absolute;width:250px;font-size:13px;line-height:19.5px}
.feature-text.left{text-align:right}
.feature-icon{position:absolute;width:58px;height:58px;background:var(--clay);transform:rotate(45deg);border-radius:10px;display:flex;align-items:center;justify-content:center}
.feature-icon svg{transform:rotate(-45deg)}
.feature-brand{position:absolute;left:457px;top:2520px;width:273px;text-align:center;color:var(--navy);font-weight:700;font-size:26px;line-height:30px}
.feature-brand i{display:block;width:110px;height:110px;margin:0 auto 40px;background:var(--navy);transform:rotate(45deg)}

/* testimonials */
.quote-card{position:absolute;top:2930px;width:290px;height:327px;background:var(--white);border-radius:0 40px 0 0;box-shadow:0 14px 34px rgba(0,0,0,.08);padding:57px 34px 0 38px}
.quote-mark{position:absolute;top:-40px;left:38px;font-family:Georgia,serif;font-size:190px;line-height:190px;color:var(--clay-soft);font-weight:700}
.quote-card p{font-size:14px;line-height:19.6px}
.quote-card h4{margin-top:30px;font-size:13px;font-weight:700;color:var(--navy)}
.quote-heading{position:absolute;left:776px;top:3010px;font-size:40px;line-height:43px}
.quote-dots{position:absolute;left:777px;top:3129px;display:flex;gap:8px}
.quote-dots i{width:6px;height:6px;border-radius:50%;background:var(--navy)}
.quote-dots i.off{background:#c7c9cd}

/* contact form */
.form-heading{position:absolute;left:0;top:3360px;width:1200px;text-align:center}
.contact-form{position:absolute;left:208px;top:3435px;width:784px;height:460px;background:var(--clay);border-radius:0 86px 0 86px}
.field label{position:absolute;font-size:10.5px;font-weight:700;color:var(--white);letter-spacing:.3px}
.field span{position:absolute;height:37px;width:181px;border-radius:19px;background:rgba(255,255,255,.22)}
.field span.area{height:116px;width:561px;border-radius:22px}
.submit{position:absolute;left:312px;top:372px;width:159px;height:43px;background:var(--white);color:var(--navy);font-size:12.5px;font-weight:700;display:flex;align-items:center;justify-content:center;border-radius:4px 20px 4px 20px}

/* footer */
.footer-brand{position:absolute;left:153px;top:4068px;color:var(--clay)}
.footer-brand .brand-name{font-size:44px;line-height:42px}
.footer-brand .brand-name small{font-size:22px;line-height:24px;letter-spacing:1.8px}
.socials{position:absolute;left:262px;top:4176px;display:flex;gap:19px}
.socials i{width:36px;height:36px;background:#505868;transform:rotate(45deg);border-radius:6px}
.footer-col h5{position:absolute;top:4054px;font-size:19px;font-weight:700;color:var(--white);letter-spacing:.3px}
.footer-col a,.footer-col div{position:absolute;font-size:14px;color:var(--white);text-decoration:none}
.footer-col svg{position:absolute}
.copyright{position:absolute;left:0;top:4336px;width:1200px;text-align:center;font-size:11px;font-weight:600;color:var(--white)}
.to-top{position:absolute;left:1088px;top:4295px;width:44px;height:44px;background:var(--clay);transform:rotate(45deg);border-radius:8px;display:flex;align-items:center;justify-content:center}
.to-top svg{transform:rotate(-45deg)}
</style>
</head>
<body>
<div class="page">

  <!-- hero backdrop -->
  <svg class="abs" style="left:0;top:80px" width="1200" height="760" viewBox="0 80 1200 760" aria-hidden="true">
    <defs>
      <linearGradient id="heroMist" x1="0" y1="0" x2="0" y2="1">
        <stop offset="0" stop-color="#e9e9ea"/><stop offset="1" stop-color="#f4f4f5"/>
      </linearGradient>
      <linearGradient id="heroPhoto" x1="0" y1="0" x2="1" y2="1">
        <stop offset="0" stop-color="#eceded"/><stop offset=".5" stop-color="#bfc2c6"/><stop offset="1" stop-color="#7a7f86"/>
      </linearGradient>
    </defs>
    <path d="M0 80H1200V820H0V560Q300 600 520 760Q300 620 0 540Z" fill="url(#heroMist)"/>
    <path d="M0 540Q300 600 560 800L0 800Z" fill="#fff"/>
    <path d="M470 80H1200V660Q1080 820 820 810Q640 800 560 700Q470 560 470 80Z" fill="url(#heroPhoto)"/>
    <path d="M700 812Q1000 840 1200 640" stroke="var(--clay-line)" stroke-width="10" fill="none"/>
  </svg>
  <div class="abs" role="img" aria-label="Photo of hands typing on a laptop beside a notebook, pen and coffee cup" style="left:520px;top:80px;width:680px;height:720px"></div>

  <header class="site-header">
    <div class="brand"><span class="brand-square"></span><div class="brand-name">MERIDIAN<small>ESCROW PARTNERS</small></div></div>
    <nav class="main-nav">
      <a class="active" style="left:547px" href="#">HOME</a>
      <a style="left:615px" href="#">ABOUT US</a>
      <a style="left:711px" href="#">SERVICES ▾</a>
      <a style="left:801px" href="#">CONTACT US</a>
    </nav>
    <div class="header-phone">
      <span class="phone-mark"><svg width="16" height="16" viewBox="0 0 24 24"><path d="M6.6 10.8a15 15 0 0 0 6.6 6.6l2.2-2.2a1 1 0 0 1 1-.25 11.4 11.4 0 0 0 3.6.57 1 1 0 0 1 1 1V20a1 1 0 0 1-1 1A17 17 0 0 1 3 4a1 1 0 0 1 1-1h3.5a1 1 0 0 1 1 1c0 1.25.2 2.45.57 3.6a1 1 0 0 1-.25 1z" fill="#fff"/></svg></span>
      555-014-2290
    </div>
  </header>

  <h1 class="hero-title">MERIDIAN<b>ESCROW</b>PARTNERS</h1>
  <p class="hero-sub">ESCROW ACCOUNTING SERVICES ARE AT THE HEART OF WHAT WE DO.</p>
  <a class="btn btn-clay" style="left:89px;top:454px;width:158px;height:44px" href="#">CONTACT US</a>
  <div class="slider-dots"><i></i><i></i><i></i></div>

  <!-- what we do -->
  <div class="abs" style="left:140px;top:745px;width:420px;height:420px;background:#fff;transform:rotate(45deg);border-radius:34px;box-shadow:0 10px 30px rgba(0,0,0,.12)"></div>
  <div class="abs" role="img" aria-label="Portrait photo of a smiling professional in a white blazer" style="left:152px;top:757px;width:396px;height:396px;transform:rotate(45deg);border-radius:80px 30px 80px 30px;background:linear-gradient(135deg,#b8b6b2,#7d7872 55%,#4a4542)"></div>
  <div class="abs" style="left:433px;top:1141px;width:64px;height:64px;background:var(--clay);transform:rotate(45deg);border-radius:10px;display:flex;align-items:center;justify-content:center">
    <svg width="18" height="18" viewBox="0 0 18 18" style="transform:rotate(-45deg)"><path d="M4 2L16 9L4 16Z" fill="#fff"/></svg>
  </div>
  <div class="about-copy">
    <h2 class="section-heading"><em>WHAT</em> WE DO</h2>
    <p>Escrow accounting services are at the heart of what we do. Trust us to provide you with peace of mind. With Meridian Escrow Partners, you can be confident that your escrow accounting will be secure, accurate, and in complete compliance with Underwriter Requirements and Best Practices.</p>
    <p class="lead">OUR TEAM OF EXPERIENCED PROFESSIONALS IS THE IDEAL SOLUTION FOR YOUR NEEDS.</p>
  </div>
  <a class="btn btn-navy" style="left:692px;top:1149px;width:158px;height:46px" href="#">LEARN MORE</a>

  <!-- services -->
  <div class="service-bar" style="top:1368px">
    <svg width="36" height="36" viewBox="0 0 36 36" fill="none" stroke="#fff" stroke-width="2"><rect x="6" y="4" width="14" height="28"/><rect x="20" y="14" width="10" height="18"/><path d="M10 10h6M10 16h6M10 22h6M23 20h4M23 26h4"/></svg>
    ECROW RECONCILIATION SERVICES
  </div>
  <div class="service-bar" style="top:1457px">
    <svg width="36" height="36" viewBox="0 0 36 36" fill="none" stroke="#fff" stroke-width="2"><circle cx="18" cy="14" r="10"/><circle cx="18" cy="14" r="5"/><path d="M12 22l-3 11 5-3 3 4 1-9M24 22l3 11-5-3-3 4"/></svg>
    NTIA BEST PRACTICE CERTIFICATION
  </div>
  <div class="service-bar" style="top:1546px">
    <svg width="36" height="36" viewBox="0 0 36 36" fill="none" stroke="#fff" stroke-width="2"><circle cx="16" cy="11" r="7"/><path d="M4 32c0-7 5-11 12-11s9 2 10 4"/><circle cx="27" cy="27" r="6" fill="#fff"/><path d="M24 27l2 2 4-4" stroke="var(--clay)"/></svg>
    DATA CALL SERVICES
  </div>
  <div class="abs" style="left:709px;top:1387px;width:260px;height:260px;background:#fff;border:2px solid var(--clay);border-radius:34px;transform:rotate(45deg)"></div>
  <div class="services-card" style="display:flex;flex-direction:column;justify-content:center">
    <h2 class="section-heading"><em>OUR</em><br>SERVICES</h2>
    <p>For professionals in the title insurance industry, finding a trustworthy and budget-friendly solution for escrow accounting can be daunting.</p>
  </div>

  <!-- team -->
  <svg class="abs" style="left:0;top:1730px" width="1200" height="606" viewBox="0 1730 1200 606" aria-hidden="true">
    <defs>
      <linearGradient id="teamPhoto" x1="0" y1="0" x2="1" y2="0">
        <stop offset="0" stop-color="#e6e6e7"/><stop offset=".35" stop-color="#6f7580"/><stop offset="1" stop-color="#2f3542"/>
      </linearGradient>
    </defs>
    <path d="M0 1840Q220 1720 500 1748L1200 1748V2336H0Z" fill="#ebebec"/>
    <path d="M0 1860Q220 1730 480 1742" stroke="var(--clay-soft)" stroke-width="10" fill="none"/>
    <path d="M520 1760L1200 1760V2336H440Q560 2100 520 1760Z" fill="url(#teamPhoto)"/>
  </svg>
  <div class="abs" role="img" aria-label="Photo of house keys being handed over a desk with a model home" style="left:480px;top:1760px;width:720px;height:576px"></div>
  <h2 class="team-heading">OUR TEAM OF<br><em>EXPERIENCED</em><br>PROFESSIONAL</h2>
  <p class="team-sub">CAN BE YOUR PERFECT SOLUTION!</p>
  <a class="btn btn-clay" style="left:89px;top:2135px;width:158px;height:44px" href="#">OUR SERVICE</a>
  <a class="btn btn-navy" style="left:264px;top:2135px;width:159px;height:44px" href="#">GET IN TOUCH</a>

  <!-- features -->
  <h2 class="section-heading abs" style="left:0;top:2415px;width:1200px;text-align:center"><em>OUR</em> FEATURES</h2>
  <p class="feature-text left" style="left:84px;top:2506px">Daily two-way reconciliation is a Best Practice Standard. Let us create a customized package that ensures your compliance and protects your reporting from audit deficiencies.</p>
  <p class="feature-text left" style="left:84px;top:2677px">We perform reconciliations across all accounting software systems using secure protocols aligning with NTIA Best Practice - Pillar 3 standards.</p>
  <p class="feature-text" style="left:853px;top:2506px">Comprehensive daily and monthly reports will be delivered securely using SecureVault. These reports will include a detailed breakdown of items that may require your attention. We also manage the submission of reconciliations to underwriters.</p>
  <p class="feature-text" style="left:853px;top:2677px">Our affordable rates allow your company to significantly enhance efficiency with minimal investment and focus on what matters. Pricing is based on account activity volume, and we offer discounts for multiple accounts.</p>
  <div class="feature-icon" style="left:363px;top:2534px"><svg width="30" height="30" viewBox="0 0 30 30" fill="none" stroke="#fff" stroke-width="3"><circle cx="15" cy="15" r="11"/><circle cx="15" cy="15" r="5"/></svg></div>
  <div class="feature-icon" style="left:363px;top:2704px"><svg width="30" height="30" viewBox="0 0 30 30"><circle cx="15" cy="15" r="10" fill="none" stroke="#fff" stroke-width="5" stroke-dasharray="4 3"/><circle cx="15" cy="15" r="4" fill="#fff"/></svg></div>
  <div class="feature-icon" style="left:766px;top:2534px"><svg width="30" height="30" viewBox="0 0 30 30" fill="#fff"><rect x="4" y="20" width="4" height="7"/><rect x="10" y="16" width="4" height="11"/><rect x="16" y="12" width="4" height="15"/><rect x="22" y="8" width="4" height="19"/><path d="M4 14L12 7l5 4 9-8" stroke="#fff" stroke-width="2" fill="none"/></svg></div>
  <div class="feature-icon" style="left:766px;top:2704px"><svg width="30" height="30" viewBox="0 0 30 30" fill="none" stroke="#fff" stroke-width="2"><text x="15" y="15" font-size="14" font-family="Montserrat,sans-serif" font-weight="700" fill="#fff" stroke="none" text-anchor="middle">$</text><path d="M3 22h6l6 3 10-5"/></svg></div>
  <div class="feature-brand"><i></i>MERIDIAN<br>ESCROW PARTNERS</div>

  <!-- testimonials -->
  <div class="quote-card" style="left:89px">
    <span class="quote-mark">“</span>
    <p>I couldn't be happier with the service at Harborline Fiduciary. They are professional and diligent and extremely helpful when I have questions or concerns. I highly recommend Harborline Fiduciary to anyone with accounting needs.</p>
    <h4>MARK ELLISON</h4>
  </div>
  <div class="quote-card" style="left:404px">
    <span class="quote-mark">“</span>
    <p>I couldn't be happier with the service at Harborline Fiduciary. They are professional and diligent and extremely helpful when I have questions or concerns. I highly recommend Harborline Fiduciary to anyone with accounting needs.</p>
    <h4>JOHN DOE</h4>
  </div>
  <h2 class="section-heading quote-heading">SEE <em>WHAT</em> OUR<br>CLIENTS THINK</h2>
  <div class="quote-dots"><i></i><i class="off"></i><i></i></div>

  <!-- contact -->
  <h2 class="section-heading form-heading">GET <em>IN</em> TOUCH</h2>
  <svg class="abs" style="left:0;top:3860px" width="1200" height="531" viewBox="0 3860 1200 531" aria-hidden="true">
    <path d="M0 4010Q420 4000 760 3940Q1000 3895 1200 3860V4391H0Z" fill="var(--navy)"/>
    <path d="M1020 3885Q1130 3870 1200 3905" stroke="var(--clay-soft)" stroke-width="10" fill="none"/>
  </svg>
  <form class="contact-form">
    <div class="field"><label style="left:111px;top:53px">NAME*</label><span style="left:111px;top:69px"></span></div>
    <div class="field"><label style="left:302px;top:53px">LAST NAME*</label><span style="left:302px;top:69px"></span></div>
    <div class="field"><label style="left:491px;top:53px">COMPANY NAME*</label><span style="left:491px;top:69px"></span></div>
    <div class="field"><label style="left:111px;top:130px">PHONE*</label><span style="left:111px;top:146px"></span></div>
    <div class="field"><label style="left:302px;top:130px">EMAIL ADDRESS*</label><span style="left:302px;top:146px"></span></div>
    <div class="field"><label style="left:491px;top:130px">STATE*</label><span style="left:491px;top:146px"></span></div>
    <div class="field"><label style="left:111px;top:205px">MESSAGE*</label><span class="area" style="left:111px;top:219px"></span></div>
    <div class="submit">SUBMIT</div>
  </form>

  <!-- footer -->
  <div class="brand footer-brand"><span class="brand-square" style="width:50px;height:50px;margin:0 10px"></span><div class="brand-name">MERIDIAN<small>ESCROW PARTNERS</small></div></div>
  <div class="socials"><i></i><i></i><i></i></div>
  <div class="footer-col">
    <h5 style="left:557px">QUICK LINKS</h5>
    <a style="left:557px;top:4100px" href="#">Home</a>
    <a style="left:557px;top:4131px" href="#">About Us</a>
    <a style="left:557px;top:4162px" href="#">Services</a>
    <a style="left:557px;top:4193px" href="#">Contact Us</a>
    <a style="left:557px;top:4224px" href="#">Privacy Policy</a>
  </div>
  <div class="footer-col">
    <h5 style="left:765px">CONTACT</h5>
    <svg style="left:762px;top:4102px" width="14" height="14" viewBox="0 0 24 24"><path d="M6.6 10.8a15 15 0 0 0 6.6 6.6l2.2-2.2a1 1 0 0 1 1-.25 11.4 11.4 0 0 0 3.6.57 1 1 0 0 1 1 1V20a1 1 0 0 1-1 1A17 17 0 0 1 3 4a1 1 0 0 1 1-1h3.5a1 1 0 0 1 1 1c0 1.25.2 2.45.57 3.6a1 1 0 0 1-.25 1z" fill="var(--clay)"/></svg>
    <div style="left:789px;top:4100px">555-014-2290</div>
    <svg style="left:762px;top:4146px" width="14" height="14" viewBox="0 0 14 14"><circle cx="7" cy="7" r="6" fill="none" stroke="var(--clay)" stroke-width="2"/><path d="M1 7h12M7 1q-4 6 0 12M7 1q4 6 0 12" stroke="var(--clay)" fill="none"/></svg>
    <div style="left:789px;top:4144px">www.meridianescrowpartners.com</div>
    <svg style="left:762px;top:4191px" width="14" height="11" viewBox="0 0 14 11"><rect width="14" height="11" rx="1" fill="var(--clay)"/><path d="M1 1l6 5 6-5" stroke="#fff" fill="none"/></svg>
    <div style="left:789px;top:4188px">hello@meridianescrow.com</div>
  </div>
  <p class="copyright">© COPYRIGHT 2024 MERIDIAN ESCROW PARTNERS, ALL RIGHTS RESERVED</p>
  <div class="to-top"><svg width="18" height="18" viewBox="0 0 18 18" fill="none" stroke="#fff" stroke-width="2"><path d="M9 16V3M3 9l6-6 6 6"/></svg></div>

</div>
</body>
</html>
```